Redesign My Travel Agency Agreements

I need my reservation request forms redesigned into a professional contract. This is a travel agency contract. Just needs to look professional. PDF format please. See attached
Target Market(s)
travel agencies and travelers
Industry/Entity Type
Travel Agency
Font styles to use
Other font styles liked:
- open
Requirements
Must have
- I need my reservation request forms redesigned into a professional contract. This is a travel agency contract. Just needs to look professional. PDF format please. See attached
Nice to have
Should not have

```html
<!DOCTYPE html>
<html lang="en">
<head>
<meta charset="utf-8">
<title>4 Night Hotel Stay – Reservation Request Form</title>
<link href="https://fonts.googleapis.com/css2?family=Poppins:wght@400;500;600;700&family=Roboto:ital,wght@1,500&family=Arimo:wght@400;700&display=swap" rel="stylesheet">
<style>
  :root {
    --backdrop: #e4e8e8;
    --paper: #f2f2f2;
    --ink: #111111;
    --accent: #f2e40a;
    --id-field: #e6e6e6;
    --rule: #222222;
  }
  * { box-sizing: border-box; margin: 0; padding: 0; }
  html, body { width: 1135px; height: 1200px; overflow: hidden; }
  body { background: var(--backdrop); color: var(--ink); font-family: 'Poppins', sans-serif; }
  .sheet {
    position: absolute; left: 127px; top: 21px;
    width: 880px; height: 1158px; background: var(--paper);
  }
  .title {
    position: absolute; left: 47px; top: 40px;
    font-weight: 700; font-size: 50px; line-height: 52px; letter-spacing: -0.5px;
  }
  .issuer, .deadlines {
    position: absolute; font-family: 'Roboto', sans-serif; font-style: italic; font-weight: 500;
    font-size: 14.5px; line-height: 19px;
  }
  .issuer { left: 47px; top: 163px; }
  .deadlines { right: 49px; top: 170px; text-align: right; }
  .deadlines .travel { margin-top: 11px; }
  .ids { position: absolute; right: 49px; top: 50px; width: 300px; }
  .id-row { display: flex; height: 27px; margin-bottom: 6px; }
  .id-label {
    width: 158px; background: var(--accent); font-weight: 500; font-size: 17px;
    line-height: 27px; padding-left: 5px;
  }
  .id-value { flex: 1; background: var(--id-field); font-size: 16.5px; line-height: 29px; padding-left: 7px; }
  .section-heading {
    position: absolute; left: 47px; top: 305px; font-weight: 500; font-size: 25px; letter-spacing: -0.2px;
  }
  .row { position: absolute; left: 47px; width: 786px; display: flex; }
  .field { display: flex; align-items: flex-end; font-size: 16px; }
  .field .line { flex: 1; border-bottom: 1.5px solid var(--rule); margin-left: 6px; margin-bottom: 5px; }
  .marker { position: absolute; left: 47px; width: 12px; height: 5px; background: var(--accent); }
  .banner {
    position: absolute; left: 47px; top: 737px; width: 782px; height: 46px;
    background: var(--accent); text-align: center; font-weight: 600; font-size: 24px; line-height: 46px;
    letter-spacing: -0.3px;
  }
  .terms { position: absolute; left: 47px; top: 810px; width: 782px; font-family: 'Arimo', sans-serif; }
  .terms h2 { font-size: 15.5px; font-weight: 700; margin-bottom: 9px; }
  .terms p { font-size: 12.35px; line-height: 16.2px; }
</style>
</head>
<body>
<main class="sheet">
  <h1 class="title">4 Night<br>Hotel Stay</h1>
  <address class="issuer">Getaway Perks<br>48 Harbor Lane<br>Suite 310<br>Portland, ME 04101</address>

  <div class="ids">
    <div class="id-row"><span class="id-label">Reservation ID #:</span><span class="id-value">1592084207</span></div>
    <div class="id-row"><span class="id-label">&nbsp;Certificate ID #:</span><span class="id-value">106719-10268</span></div>
    <div class="id-row"><span class="id-label">&nbsp;Issue Date:</span><span class="id-value">12/11/2020</span></div>
  </div>
  <div class="deadlines">
    <p>Submit Your<br>Reservation Request Form By: 06/13/2020</p>
    <p class="travel">Travel Must Be Completed By: 06/13/2022</p>
  </div>

  <h2 class="section-heading">CUSTOMER INFORMATION</h2>

  <div class="row" style="top:354px">
    <div class="field" style="width:401px">First Name<span class="line"></span></div>
    <div class="field" style="width:385px;padding-left:8px">Last Name<span class="line"></span></div>
  </div>
  <div class="row" style="top:392px">
    <div class="field" style="width:339px;padding-left:2px">Phone<span class="line"></span></div>
    <div class="field" style="width:447px;padding-left:11px;padding-top:3px">Email<span class="line"></span></div>
  </div>
  <span class="marker" style="top:436px"></span>
  <div class="row" style="top:458px">
    <div class="field" style="width:382px;padding-left:2px">Traveler 1 Name<span class="line"></span></div>
    <div class="field" style="width:404px;padding-left:9px">Traveler 2 Name<span class="line"></span></div>
  </div>
  <div class="row" style="top:498px">
    <div class="field" style="width:382px;padding-left:2px">Traveler 3 Name<span class="line"></span></div>
    <div class="field" style="width:404px;padding-left:9px">Traveler 4 Name<span class="line"></span></div>
  </div>
  <span class="marker" style="top:550px"></span>
  <div class="row" style="top:566px">
    <div class="field" style="width:246px;padding-left:2px">Arrival Date #1:<span class="line"></span></div>
    <div class="field" style="width:269px;padding-left:14px">Arrival Date #2:<span class="line"></span></div>
    <div class="field" style="width:271px;padding-left:15px">Arrival Date #3:<span class="line"></span></div>
  </div>
  <div class="row" style="top:610px">
    <div class="field" style="width:377px;padding-left:2px">Destination#1:<span class="line"></span></div>
    <div class="field" style="width:409px;padding-left:16px">Destination#2:<span class="line"></span></div>
  </div>
  <div class="row" style="top:651px">
    <div class="field" style="width:383px;padding-left:2px">Destination#3:<span class="line"></span></div>
    <div class="field" style="width:403px;padding-left:13px">Alternate Destination:<span class="line"></span></div>
  </div>

  <div class="banner">RESERVATION REQUEST FORM</div>

  <section class="terms">
    <h2>TERMS AND CONDITIONS:</h2>
    <p>This reservation request form will be considered void if bartered or sold to the recipient.&nbsp; This reservation request form is offering 2 adults 21 years of age and older plus up to 2 children under the age of 18 up to 4 nights of hotel accommodations in the city of your choice of available cities.&nbsp; The cost upon requesting reservations is a tax &amp; fee deposit of $33 per night.&nbsp; Taxes &amp; fees usually range from $12-$33 per night depending on when and where you travel.&nbsp; If the taxes &amp; fees are less than the $33 per night the difference will be refunded after travel is completed.&nbsp; All reservations require a minimum of 30 days advance notice.&nbsp; In order to guarantee you will show up to your booked reservation you will be required to pay a REFUNDABLE $50 Reservation Guarantee Deposit.&nbsp; Dates near holidays and during major conventions or events are usually not available.&nbsp; All vacation offers are subject to the fulfilling travel agencies availability and promotions inventory.&nbsp; This offer is valid 7 days a week.&nbsp; Friday and Saturday nights will require a surcharge of $20 per night.&nbsp; A $5 per person per night surcharge is enforced for 3rd and 4th persons.&nbsp; Transportation and meals are not included with this offer.&nbsp; This offer is not valid for group travel.&nbsp; The recipient of this reservation request form is responsible for all expenses including but not limited to: transfers, food, gratuities, all pertinent fees, taxes, hotel/resort surcharges and any other miscellaneous expenses.&nbsp; This reservation request form cannot be combined with any other promotional vacation offer.&nbsp; You must fill out the reservation request form with your destination choices, arrival dates and mail it to our fulfillment department within 6 months after redemption, however, travel must be completed within 24 months after redemption.&nbsp; In most cases you will be required to give the travel agency multiple arrival dates just in case your 1st requested arrival dates are not available.&nbsp; Only one 4 Night Hotel offer Per Household Per Year.&nbsp; Lost or stolen reservation request forms will not be replaced.&nbsp; This reservation request form has no cash surrender value, void if discontinued and where prohibited by law.&nbsp; The terms of this offer are subject to change without notice.</p>
  </section>
</main>
</body>
</html>
```